Business Card Design Project

This is the first time we use our new logo. We need a business card that we can use both on our institutional corporate relationships and also that works for our staff that deals with consumers directly.

VELUNDA is a new company dedicated to empower consumers and to provide them with the best choices for specialized health care using the latest telemedicine technology (medicine at a distance via videoconference).

We want to print this cards in high quality materials and process. We will like designs that allow us to use UV spot varnish and other techniques that will differentiate us.

We are including Two different versions of Color logos. In addition we are including white over black background logos. Those can be used replacing the black for a color.

Please note this is the first time we will be creating any corporate materials with our new logo and colors.

Target Market(s)

34+ consumers of medium high and high socioeconomic levels.

Industry/Entity Type

Health

Requirements
Must have
• Our logo on its original colors
Should not have
• Any other graphical element or design that is not our logo

```html
<!DOCTYPE html>
<html lang="en">
<head>
<meta charset="utf-8">
<title>VELUNDA Business Card</title>
<link rel="stylesheet" href="https://fonts.googleapis.com/css2?family=Playfair+Display+SC:wght@400;700&display=swap">
<style>
  :root {
    --bg: #e9ecef;
    --card: #ffffff;
    --teal: #1fb3b0;
    --teal-light: #8fd8e6;
    --sky: #4aa6dc;
    --navy: #23267a;
    --navy-deep: #15164f;
    --label: #4a7fae;
    --ink: #2f3336;
    --brand: #1f5a7e;
    --ring-faint: #dcebf3;
    --shade: #c9c6c2;
  }
  * { margin: 0; padding: 0; box-sizing: border-box; }
  html, body { width: 1200px; height: 750px; overflow: hidden; background: var(--bg); }
  .canvas { position: relative; width: 1200px; height: 750px; }
  .card {
    position: absolute;
    left: 305px;
    width: 598px;
    height: 313px;
    background: var(--card);
    border-radius: 16px;
    overflow: hidden;
    box-shadow: 0 6px 18px rgba(0,0,0,0.18);
  }
  .card--front { top: 41px; }
  .card--back { top: 392px; }
  .card__waves { position: absolute; inset: 0; width: 100%; height: 100%; }
  .contact {
    position: absolute;
    left: 22px;
    top: 152px;
    font-family: "Playfair Display SC", Georgia, serif;
    font-weight: 700;
  }
  .contact__name { font-size: 24px; color: #4e5357; letter-spacing: 0.5px; padding-left: 10px; }
  .contact__role { font-size: 15px; color: var(--label); padding-left: 70px; margin-top: -2px; }
  .contact__list { list-style: none; margin-top: 8px; }
  .contact__item { font-size: 15px; line-height: 24.5px; color: var(--ink); }
  .contact__label { color: var(--label); }
  .front-accent {
    position: absolute;
    right: 26px;
    top: 182px;
    width: 104px;
    height: 104px;
    border-radius: 50%;
    border: 12px solid var(--ring-faint);
  }
  .brand {
    position: absolute;
    left: 48px;
    top: 78px;
    display: flex;
    align-items: center;
    gap: 22px;
  }
  .brand__dot {
    width: 92px;
    height: 92px;
    border-radius: 50%;
    background: var(--teal);
  }
  .brand__name {
    font-family: "Playfair Display SC", Georgia, serif;
    font-weight: 700;
    font-size: 62px;
    letter-spacing: 3px;
    color: var(--brand);
  }
</style>
</head>
<body>
<main class="canvas">

  <section class="card card--front" aria-label="Card front with contact details">
    <svg class="card__waves" viewBox="0 0 598 313" preserveAspectRatio="none" aria-hidden="true">
      <defs>
        <linearGradient id="front-sky" x1="0" y1="0" x2="0" y2="1">
          <stop offset="0" stop-color="#1fb3b0"/>
          <stop offset="0.55" stop-color="#5cc3e0"/>
          <stop offset="1" stop-color="#a9e0ef"/>
        </linearGradient>
        <linearGradient id="front-swoosh" x1="0" y1="0" x2="1" y2="0">
          <stop offset="0" stop-color="#4a4fb8"/>
          <stop offset="0.5" stop-color="#23267a"/>
          <stop offset="1" stop-color="#15164f"/>
        </linearGradient>
        <linearGradient id="front-blue" x1="0" y1="0" x2="1" y2="0">
          <stop offset="0" stop-color="#2b7fd0"/>
          <stop offset="1" stop-color="#4aa6dc"/>
        </linearGradient>
      </defs>
      <rect width="598" height="313" fill="url(#front-sky)"/>
      <path d="M70,0 C170,60 270,112 390,122 C480,130 550,150 598,168 L598,120 C530,98 470,84 400,80 C290,72 190,30 140,0 Z" fill="url(#front-blue)"/>
      <path d="M20,0 C140,70 250,120 380,128 C480,134 550,160 598,182 L598,160 C540,138 470,118 390,110 C270,98 170,40 110,0 Z" fill="url(#front-swoosh)"/>
      <path d="M0,165 C110,150 200,112 300,112 C420,112 500,150 598,205 L598,313 L0,313 Z" fill="var(--shade)" opacity="0.55"/>
      <path d="M0,172 C110,158 200,122 300,122 C420,122 500,160 598,212 L598,313 L0,313 Z" fill="#ffffff"/>
    </svg>

    <div class="contact">
      <p class="contact__name">Darren Holvik</p>
      <p class="contact__role">President</p>
      <ul class="contact__list">
        <li class="contact__item"><span class="contact__label">Adress:</span> Marsten Lane</li>
        <li class="contact__item"><span class="contact__label">Mobile:</span> 55510 482 617</li>
        <li class="contact__item"><span class="contact__label">E-mail:</span> dholvik@velunda.example</li>
        <li class="contact__item"><span class="contact__label">Website:</span> www.velunda.example</li>
      </ul>
    </div>
    <div class="front-accent" aria-hidden="true"></div>
  </section>

  <section class="card card--back" aria-label="Card back with company name">
    <svg class="card__waves" viewBox="0 0 598 313" preserveAspectRatio="none" aria-hidden="true">
      <defs>
        <linearGradient id="back-sea" x1="0" y1="0" x2="0" y2="1">
          <stop offset="0" stop-color="#5cc3e0"/>
          <stop offset="0.5" stop-color="#1fb3b0"/>
          <stop offset="1" stop-color="#8fd8e6"/>
        </linearGradient>
        <linearGradient id="back-swoosh" x1="1" y1="0" x2="0" y2="0">
          <stop offset="0" stop-color="#15164f"/>
          <stop offset="0.6" stop-color="#23267a"/>
          <stop offset="1" stop-color="#4a4fb8"/>
        </linearGradient>
        <linearGradient id="back-blue" x1="0" y1="0" x2="1" y2="0">
          <stop offset="0" stop-color="#4aa6dc"/>
          <stop offset="1" stop-color="#2b7fd0"/>
        </linearGradient>
      </defs>
      <rect width="598" height="313" fill="url(#back-sea)"/>
      <path d="M598,175 C500,205 400,215 300,225 C180,238 80,262 0,300 L0,313 L60,313 C140,275 220,258 320,248 C430,238 520,222 598,205 Z" fill="url(#back-blue)"/>
      <path d="M598,170 C500,200 400,208 300,216 C180,228 80,255 0,290 L0,300 C90,268 190,245 310,236 C420,228 520,212 598,196 Z" fill="url(#back-swoosh)"/>
      <path d="M0,0 H598 V165 C520,190 440,198 360,200 C240,203 130,182 0,205 Z" fill="#ffffff"/>
    </svg>

    <div class="brand">
      <span class="brand__dot" aria-hidden="true"></span>
      <span class="brand__name">VELUNDA</span>
    </div>
  </section>

</main>
</body>
</html>
```